Tellborne Medical

Need smart and sleek business cards design for my medical distribution company. use logos attached.

add my details

Lorcan Pettifer
Director/Sales Agent
lorcan@tellbornemedical-example.com.au
0491 638 170

```html
<!DOCTYPE html>
<html lang="en">
<head>
<meta charset="utf-8">
<title>Tellborne Medical – Business Cards</title>
<link href="https://fonts.googleapis.com/css2?family=Arimo:wght@400;700&display=swap" rel="stylesheet">
<style>
  :root {
    --navy: #1f2a5e;
    --navy-deep: #1a2452;
    --sky: #2a87bb;
    --white: #ffffff;
    --backdrop: #3a3b3d;
  }
  * { margin: 0; padding: 0; box-sizing: border-box; }
  html, body {
    width: 1200px; height: 915px; overflow: hidden;
    background: var(--backdrop);
    font-family: "Arimo", Arial, sans-serif;
  }
  .canvas { position: relative; width: 1200px; height: 915px; }

  .card {
    position: absolute;
    left: 290px;
    width: 620px; height: 354px;
    border-radius: 18px;
    overflow: hidden;
    background: var(--navy);
    color: var(--white);
  }
  .card--front { top: 70px; }
  .card--back  { top: 490px; }

  /* Front */
  .front-brand {
    position: absolute; inset: 0;
    display: flex; align-items: center; justify-content: center; gap: 18px;
  }
  .brand-dot { width: 22px; height: 22px; border-radius: 50%; background: var(--white); }
  .brand-name {
    font-weight: 700; font-size: 50px; letter-spacing: 1px; color: var(--white);
  }

  /* Back */
  .back-info {
    position: absolute; left: 0; top: 0; width: 354px; height: 100%;
    padding: 34px 0 0 34px;
  }
  .back-brand {
    display: flex; align-items: center; gap: 10px;
    font-weight: 700; font-size: 24px; color: var(--white);
  }
  .back-brand .brand-dot { width: 12px; height: 12px; }
  .person-name { margin-top: 86px; font-weight: 700; font-size: 27px; }
  .person-role { margin-top: 6px; font-size: 15px; }
  .contacts { margin-top: 58px; list-style: none; font-size: 15px; }
  .contacts li { display: flex; align-items: center; gap: 10px; margin-top: 8px; }
  .contacts svg { width: 15px; height: 15px; flex: none; }

  .divider {
    position: absolute; left: 354px; top: 0; width: 5px; height: 100%;
    background: var(--white);
  }
  .symbol-panel {
    position: absolute; left: 359px; top: 0; right: 0; bottom: 0;
    background: linear-gradient(160deg, var(--navy-deep) 0%, var(--navy) 45%, var(--white) 46%, var(--white) 62%, var(--sky) 63%, var(--sky) 100%);
  }
</style>
</head>
<body>
<div class="canvas">
  <section class="card card--front">
    <div class="front-brand">
      <span class="brand-dot"></span>
      <span class="brand-name">Tellborne Medical</span>
    </div>
  </section>

  <section class="card card--back">
    <div class="back-info">
      <div class="back-brand"><span class="brand-dot"></span>Tellborne Medical</div>
      <div class="person-name">Lorcan Pettifer</div>
      <div class="person-role">Director/Sales Agent</div>
      <ul class="contacts">
        <li>
          <svg viewBox="0 0 16 16" aria-hidden="true"><path fill="#fff" d="M3 1l3 3-2 2c1 2 3 4 5 5l2-2 3 3-2 2C7 15 1 9 1 3z"/></svg>
          0491 638 170
        </li>
        <li>
          <svg viewBox="0 0 16 16" aria-hidden="true"><rect x="1" y="3" width="14" height="10" fill="none" stroke="#fff" stroke-width="1.5"/><path d="M1 3l7 6 7-6" fill="none" stroke="#fff" stroke-width="1.5"/></svg>
          lorcan@tellbornemedical-example.com.au
        </li>
      </ul>
    </div>
    <div class="divider"></div>
    <div class="symbol-panel" role="img" aria-label="Large brand symbol decoration in navy, white and sky blue"></div>
  </section>
</div>
</body>
</html>
```